Let's Play Zaplorer Re-Design, Into Video, Zaplora Icon, Banner, etc

A popular niche zaplorer is looking for design ideas to bring his channel into 2022 with a bang. His bread and butter is survival type games, this could be island style survival, zombie apocalypse survival, etc.

The K that is used for the icon bubble is iconic, and would benefit from a refresh, without too much of a design change.

Intro should be limited to about 4-5 seconds.

You can get an idea of the channel on zaplora here: Zaplora-dot-com/user/Rovin317
Updates

I'm requesting to extend this deadline to allow designers more time to gather information from the current zaplora channel at https://www.zaplora.com/user/Rovin317 as well as submit a good design they're proud of. I do have plans on being on vacation for 4 days as well, this is due to a family emergency.

Low designer entries

I've increased the deadline, increased the first place pick and added two participation spots in hopes to get more designs. If there are any questions please feel free to reach out to me. Thanks,

Target Market(s)

Zaplora Members and Viewers

Requirements
Must have
• New Video Intro, Zaplora Icon, Banner

```html
<!DOCTYPE html>
<html lang="en">
<head>
<meta charset="utf-8">
<title>Rovin317 Channel Banner</title>
<link rel="stylesheet" href="https://fonts.googleapis.com/css2?family=Russo+One&family=Michroma&family=Roboto+Condensed:wght@700&display=swap">
<style>
  :root {
    --page: #ffffff;
    --night: #000000;
    --smoke: #25272b;
    --haze: #45403d;
    --rust: #4e3b32;
    --dusk-blue: #2c3a48;
    --stripe-red: #e0261f;
    --stripe-blue: #2f7fa6;
    --steel: #c9d6de;
    --button-red: #d8221c;
    --white: #ffffff;
  }
  * { margin: 0; padding: 0; box-sizing: border-box; }
  html, body {
    width: 891px;
    height: 1200px;
    overflow: hidden;
    background: var(--page);
  }
  .canvas {
    position: relative;
    width: 891px;
    height: 1200px;
  }
  .banner {
    position: absolute;
    left: 89px;
    top: 400px;
    width: 713px;
    height: 401px;
    background: var(--night);
    overflow: hidden;
  }
  .ruined-city {
    position: absolute;
    left: 0;
    top: 85px;
    width: 713px;
    height: 225px;
    background:
      radial-gradient(ellipse 22% 35% at 18% 30%, var(--rust) 0%, transparent 80%),
      radial-gradient(ellipse 30% 45% at 52% 40%, var(--haze) 0%, transparent 80%),
      radial-gradient(ellipse 28% 50% at 85% 55%, var(--dusk-blue) 0%, transparent 80%),
      radial-gradient(ellipse 20% 35% at 62% 85%, #3a302c 0%, transparent 80%),
      linear-gradient(180deg, transparent 0%, var(--smoke) 30%, #1d1e21 70%, transparent 100%);
  }
  .survivor-figure {
    position: absolute;
    left: 252px;
    top: 167px;
    width: 74px;
    height: 150px;
    border-radius: 36px 36px 12px 12px;
    background: linear-gradient(180deg, #4d3a33 0%, #3a2a27 55%, rgba(0,0,0,0) 100%);
  }
  .stripes { position: absolute; left: 0; top: 0; }
  .channel-mark {
    position: absolute;
    left: 195px;
    top: 167px;
    width: 62px;
    height: 62px;
    border-radius: 50%;
    border: 3px solid var(--stripe-blue);
    background: rgba(20, 50, 70, 0.7);
  }
  .channel-name {
    position: absolute;
    left: 372px;
    top: 168px;
    font-family: "Russo One", sans-serif;
    color: var(--steel);
    line-height: 1;
  }
  .channel-name .name-top {
    display: block;
    font-size: 23px;
    letter-spacing: 3px;
  }
  .channel-name .name-bottom {
    display: block;
    font-size: 46px;
    letter-spacing: 8px;
    margin-top: -2px;
  }
  .social-handle {
    position: absolute;
    left: 110px;
    top: 216px;
    font-family: "Michroma", sans-serif;
    font-size: 8px;
    color: var(--white);
    letter-spacing: 0.5px;
  }
  .subscribe-button {
    position: absolute;
    left: 534px;
    top: 208px;
    width: 76px;
    height: 16px;
    border-radius: 8px;
    background: var(--button-red);
    border: 1px solid #ff6b5e;
    display: flex;
    align-items: center;
    gap: 3px;
    padding-left: 4px;
    font-family: "Roboto Condensed", sans-serif;
    font-weight: 700;
    font-size: 11px;
    color: var(--white);
  }
  .subscribe-button .bell {
    width: 9px;
    height: 9px;
    border-radius: 50%;
    background: var(--white);
  }
</style>
</head>
<body>
<div class="canvas">
  <section class="banner">
    <div class="ruined-city" role="img" aria-label="Dark ruined city skyline with smoke and a broken temple"></div>
    <svg class="stripes" width="713" height="401" viewBox="0 0 713 401" aria-hidden="true">
      <rect x="0" y="184" width="196" height="4" fill="var(--stripe-red)"/>
      <rect x="0" y="246" width="713" height="2" fill="var(--stripe-blue)"/>
      <rect x="384" y="254" width="329" height="5" fill="var(--stripe-red)"/>
    </svg>
    <div class="survivor-figure" role="img" aria-label="Illustrated survivor with a wounded face, turned to the right"></div>
    <svg class="stripes" width="713" height="401" viewBox="0 0 713 401" aria-hidden="true">
      <polygon points="318,176 336,170 392,259 372,259" fill="var(--stripe-red)"/>
    </svg>
    <div class="channel-mark" aria-hidden="true"></div>
    <div class="social-handle">@ROVIN317</div>
    <div class="channel-name"><span class="name-top">ROVIN</span><span class="name-bottom">317</span></div>
    <div class="subscribe-button"><span class="bell"></span>SUBSCRIBE</div>
  </section>
</div>
</body>
</html>
```